Creative Report - A Presentation

We are looking for a report to visual workers' compensation claim data and the impact claims have on premium. I’m looking for something that is very visually new, appealing, easy to understand, and cutting edge.

Right now we are looking for 6 pages to be designed: a cover page, an informative page, and 4 reports. The key data for the last 3 reports are listed in the other document attached named “Key Data for Report”. These should be designed in a 8.5 x 11 page layout.

I would prefer a way where things can be combined without looking too crowded. You can play around with the background, for printing purposes try to leave white space.

Attached are a few graphs that I found that I like the look of. Please design when YOU think is best. The docx & the comments on the side are just to help you visualize.

We are a mod analysis company that is always developing new reports. We are hoping to find a designer we can work with in the future as well – think of this as a trial run!

2 designers reached out this morning wanting to submit designs, I would like to see what they have.

```html
<!DOCTYPE html>
<html lang="en">
<head>
<meta charset="utf-8">
<title>Workers Compensation Executive Summary</title>
<link href="https://fonts.googleapis.com/css2?family=Bebas+Neue&family=Poppins:wght@400;500;600;700&display=swap" rel="stylesheet">
<style>
:root{
  --canvas:#ebebeb;
  --paper:#ffffff;
  --navy:#0f1f4b;
  --blue:#2f95d0;
  --bright:#1f8ae0;
  --ink:#333a45;
  --muted:#555c66;
  --cell:#d6d6d6;
  --cell-light:#ececec;
  --panel:#cfcfcf;
  --green:#3fd62a;
  --red:#e3221c;
  --yellow:#f8c21a;
  --mint:#35d07a;
}
*{margin:0;padding:0;box-sizing:border-box}
html,body{width:1200px;height:2327px;overflow:hidden;background:var(--canvas);font-family:"Poppins",sans-serif;color:var(--ink)}
.page{position:absolute;width:467px;height:604px;background:var(--paper);box-shadow:0 2px 6px rgba(0,0,0,.18);overflow:hidden}
.abs{position:absolute}
.small{font-size:6.3px;line-height:1.3;color:var(--muted)}
.small b{color:var(--ink)}
.page-head{position:absolute;top:27px;left:0;right:0;height:19px;border-bottom:3px solid var(--navy)}
.page-head .tab{display:inline-block;height:19px;background:var(--navy);color:#fff;font-weight:600;font-size:12.5px;line-height:19px;padding:0 26px 0 27px;clip-path:polygon(0 0,calc(100% - 14px) 0,100% 100%,0 100%)}
.brand{position:absolute;right:27px;bottom:30px;display:flex;align-items:center;gap:5px;font-weight:600;font-size:12px;color:var(--blue);letter-spacing:1px}
.brand i{display:block;width:9px;height:9px;background:var(--blue)}
.disclaimer{position:absolute;left:27px;font-size:7.5px;font-weight:500;color:var(--ink)}
.section-title{position:absolute;font-size:12px;font-weight:500;color:var(--navy)}
.section-title.ruled{border-bottom:1.5px solid var(--blue);padding-bottom:3px}
.photo{position:absolute}
/* cover */
.cover-photo{left:0;top:0;width:467px;height:330px;background:linear-gradient(120deg,#d9cbb4 0%,#b9a37e 30%,#e9e1d2 55%,#7f9a4c 75%,#f2d6d2 100%)}
.cover-title{position:absolute;left:27px;top:235px;font-family:"Bebas Neue",sans-serif;font-weight:400;font-size:61px;line-height:54px;color:var(--navy)}
.cover-mod{position:absolute;left:27px;top:413px;font-weight:500;font-size:22px;color:#444}
.cover-note{position:absolute;left:27px;top:440px;font-size:10.5px;color:#555}
.name-bar{position:absolute;left:0;top:516px;width:187px;height:19px;background:var(--blue);color:#fff;font-weight:600;font-size:14px;line-height:19px;padding-left:27px}
.contact{position:absolute;left:27px;font-size:10px;font-weight:500;color:#444}
/* info page */
.they-box{position:absolute;left:28px;top:104px;width:412px;height:90px;border:1.5px solid var(--navy);border-left:none;border-radius:0 8px 8px 0}
.they-box h3{position:absolute;left:0;top:-9px;background:#fff;padding-right:6px;font-size:11px;font-weight:500;color:var(--navy)}
.they-box .cap{position:absolute;left:0;bottom:-4px;width:18px;height:6px;border-radius:3px;background:var(--navy)}
.bullets{list-style:none}
.bullets li{position:relative;padding-left:18px;font-size:7px;line-height:1.3;color:#444;margin-bottom:10px}
.bullets li::before{content:"";position:absolute;left:0;top:2px;width:5px;height:5px;border-radius:50%;background:var(--blue)}
.osha{position:absolute;left:28px;top:230px;width:412px;height:151px;border-radius:8px;overflow:hidden;background:var(--panel)}
.osha h4{background:var(--blue);color:#fff;font-size:11px;font-weight:500;line-height:1.3;padding:3px 12px}
.osha .body{padding:10px 12px 0}
.osha .bullets li{font-size:6.6px;padding-left:14px;margin:6px 0}
.osha .bullets li::before{width:4px;height:4px}
/* gauge */
.gauge-zone{position:absolute;left:0;top:72px;width:467px;height:115px;background:linear-gradient(90deg,#fff 0%,#f1f1f1 50%,#fff 100%)}
.gauge{position:absolute;left:72px;top:50px;width:327px;height:14px;border-radius:7px;background:#c8c8c8;border:1px solid #888}
.gauge .fill{position:absolute;left:33px;top:0;width:210px;height:12px;background:linear-gradient(90deg,#3ed82a 0%,#8ee614 35%,#e6ea12 55%,#f6a71b 75%,#e61f1c 100%)}
.gauge .mid{position:absolute;left:162px;top:-6px;width:1px;height:24px;background:#555}
.tag{position:absolute;color:#fff;font-size:8px;font-weight:700;padding:1px 5px;border-radius:2px}
.tag-label{position:absolute;font-size:6.5px;font-weight:700;color:#222}
/* donuts & callouts */
.callout{position:absolute;border-radius:6px;color:#fff;padding:0 8px 6px}
.callout .hd{font-size:6.5px;font-weight:600;text-align:center;padding:3px 4px;margin:0 -8px 6px;border-radius:6px 6px 0 0}
.callout ul{list-style:none}
.callout li{position:relative;font-size:6.6px;line-height:1.25;padding-left:7px;margin-bottom:8px}
.callout li::before{content:"";position:absolute;left:0;top:2px;width:3px;height:3px;border-radius:50%;background:#fff}
.arrow-list{list-style:none}
.arrow-list li{position:relative;padding-left:16px;font-size:7px;color:#333;margin-bottom:6px}
.arrow-list li::before{content:"";position:absolute;left:0;top:2px;border-left:5px solid var(--blue);border-top:3px solid transparent;border-bottom:3px solid transparent}
/* tables */
.data-table{position:absolute;border-collapse:separate;border-spacing:11px 1px;font-size:6.4px;color:#222}
.data-table th{background:var(--blue);color:#fff;font-weight:500;font-size:6.5px;line-height:1.1;padding:3px 4px;text-align:left;border-radius:3px 3px 0 0;vertical-align:middle}
.data-table td{padding:2px 4px;text-align:center;height:13px}
.data-table td:first-child{text-align:left}
.data-table tr:nth-child(odd) td{background:var(--cell-light)}
.data-table tr:nth-child(even) td{background:var(--cell)}
.legend{list-style:none;font-size:6.8px;color:#333}
.legend li{display:flex;align-items:center;gap:8px;margin-bottom:6px}
.legend i{display:block;width:7px;height:7px}
.band{position:absolute;left:0;width:467px;background:var(--blue)}
</style>
</head>
<body>

<section class="page" style="left:80px;top:129px">
  <div class="photo cover-photo" role="img" aria-label="Photo of two business people shaking hands"></div>
  <svg class="abs" style="left:0;top:0" width="467" height="410" viewBox="0 0 467 410">
    <polygon points="0,229 276,229 344,319 467,319 467,404 0,404" fill="#1f8ae0"/>
    <rect x="0" y="405" width="467" height="2" fill="#ffffff"/>
  </svg>
  <div class="abs" style="left:0;top:408px;width:467px;height:196px;background:linear-gradient(160deg,#ffffff 0%,#f3f3f3 60%,#ffffff 100%)"></div>
  <h1 class="cover-title">Workers<br>Compensation<br>Executive Summary</h1>
  <div class="cover-mod">MOD EFFECTIVE 10-08-2022</div>
  <div class="cover-note">(This document uses proposed rating values that are not yet final.)</div>
  <div class="name-bar">HARLAN BECK</div>
  <div class="contact" style="top:542px">Phone - 555 014 2207</div>
  <div class="contact" style="top:560px">Email - h.beck@example.com</div>
  <div class="brand" style="bottom:38px;font-size:15px"><i></i>LEDGERWAY</div>
</section>

<section class="page" style="left:660px;top:129px">
  <div class="page-head"><span class="tab" style="width:299px">WORKERS COMPENSATION</span></div>
  <p class="abs small" style="left:28px;top:60px;width:412px">Workers Compensation claims can have a significant impact on a business. In addition to the direct claim costs, there are many other costs associated with a workers compensation claim that can impact a business.</p>
  <div class="they-box">
    <h3>They are</h3>
    <ul class="bullets abs" style="left:0;top:13px;width:180px">
      <li>Work Comp Premium Costs.</li>
      <li>Overtime.</li>
      <li>Administrative time spent on claim after an injury.</li>
    </ul>
    <ul class="bullets abs" style="left:210px;top:13px;width:190px">
      <li style="font-size:8px">Lost Opportunities due to staffing.</li>
      <li style="font-size:8px;margin-top:12px">Lost Productivity.</li>
      <li style="font-size:8px;margin-top:12px">Clean up or repair of damaged equipment.</li>
    </ul>
    <span class="cap"></span>
  </div>
  <div class="osha">
    <h4>OSHA estimates that depending upon the size of the claim indirect costs range from 1 to 4 times the direct costs.</h4>
    <div class="body">
      <p class="small" style="color:#444">The following report explains in detail how a workers compensation claim affects the premium that your business pays for workers compensation. Most business have an experience mod that is reflective of their past claims experience and every claim has an impact on the experience mod. It is important to note that some claims affect the mod differently.</p>
      <ul class="bullets">
        <li>A medical only claim is reduced by 70% in the mod calculation.</li>
        <li>A medical/indemnity claim has no reduction.</li>
        <li>All claims are also limited by a primary threshold value where claims are grouped into primary claims and excess claims.</li>
      </ul>
    </div>
  </div>
  <p class="abs small" style="left:28px;top:406px;width:412px">The following report will analyze the types of claims that are occurring in your business and will group them together for ease of identifying trends and areas of opportunity to improve.</p>
  <p class="abs small" style="left:28px;top:433px;width:412px">By identifying the types and causes of losses many times a cost/benefit analysis can be performed to allow for safety training, additional equipment or building or process improvements.</p>
  <p class="abs small" style="left:28px;top:460px;width:412px">For the premium cost analysis in this report we have used a manual premium of $XXX,XXX. A manual premium is the premium derived by the carrier before any credits, debits, or experience rating.</p>
  <div class="disclaimer" style="top:514px">DISCLAIMER</div>
  <div class="brand"><i></i>LEDGERWAY</div>
</section>

<section class="page" style="left:80px;top:830px">
  <div class="page-head"><span class="tab" style="width:205px">YOUR EXPERIENCE MOD</span></div>
  <p class="abs small" style="left:27px;top:56px">The report below shows your company's actual experience mod as well as your lowest possible mod.</p>
  <div class="gauge-zone">
    <div class="tag-label" style="left:294px;top:13px">Actual Mod</div>
    <div class="tag" style="left:302px;top:24px;background:var(--red)">1.19</div>
    <svg class="abs" style="left:311px;top:37px" width="10" height="6"><polygon points="0,0 10,0 5,6" fill="#e3221c"/></svg>
    <div class="gauge"><div class="fill"></div><div class="mid"></div></div>
    <svg class="abs" style="left:105px;top:78px" width="10" height="6"><polygon points="0,6 10,6 5,0" fill="#3fd62a"/></svg>
    <div class="tag" style="left:96px;top:84px;background:var(--green);color:#111">0.62</div>
    <div class="tag-label" style="left:89px;top:98px">Min Mod</div>
  </div>
  <h3 class="section-title ruled" style="left:27px;top:191px">MOD Value Explanation</h3>
  <p class="abs small" style="left:27px;top:218px;width:400px">A mod value <b>below 1.0</b> means your company is performing better than your peers. If your company had no claims your lowest possible mod value would be <b>0.632</b></p>
  <p class="abs small" style="left:27px;top:244px">A mod of <b>1.0 is considered average.</b></p>
  <p class="abs small" style="left:27px;top:262px;width:380px">A mod value <b>above 1.0</b> means your company is <b>performing worse</b> than your peers and you will pay more in workers compensation premium.</p>
  <h3 class="section-title ruled" style="left:27px;top:289px">Summary</h3>
  <p class="abs small" style="left:27px;top:315px;width:400px">The incurred claims reported have a <b>claim impact of 0.56</b> on your mod value. This is increasing your premium annually by <b>$112,000.</b></p>
  <p class="abs small" style="left:27px;top:342px;width:400px">In the following pages we'll dig into the types of claims your business is having and look for areas of opportunity to reduce or eliminate claims and lower your mod value.</p>
  <div class="band" style="top:392px;height:86px"></div>
  <div class="photo" role="img" aria-label="Photo of a team stacking hands together over a digital interface" style="left:65px;top:379px;width:344px;height:115px;border:2px solid #1d5fa8;background:linear-gradient(110deg,#1e3e6e 0%,#7fa6cf 40%,#c9d8e8 55%,#4f78a6 80%,#24446f 100%)"></div>
  <div class="disclaimer" style="top:522px">DISCLAIMER</div>
  <div class="brand"><i></i>LEDGERWAY</div>
</section>

<section class="page" style="left:660px;top:830px">
  <div class="page-head"><span class="tab" style="width:322px">MEDICAL VS MEDICAL/INDEMNITY CLAIMS</span></div>
  <p class="abs small" style="left:27px;top:60px;width:405px">The type of claims your business is having can have a significant impact on your mod value as not all claims are valued equally. Medical only claims have their value reduced by 70% in the mod calculation and any claim with an indemnity payment is not reduced. This is one of the reasons an effective return to work program can help reduce your premium costs.</p>
  <p class="abs" style="left:27px;top:111px;font-size:8.5px;font-weight:600;color:#222">Here's your company's breakdown.</p>
  <ul class="arrow-list abs" style="left:27px;top:129px">
    <li>The total losses for the period reviewed are <b>$284,623.</b></li>
    <li>Medical only claims accounted for <b>$85,719 in losses.</b></li>
    <li>Medical/Indemnity claims accounts for <b>$198,904 in losses.</b></li>
  </ul>
  <div class="abs" style="left:0;top:186px;width:467px;height:186px;background:linear-gradient(90deg,#fff 0%,#f0f0f0 60%,#fff 100%)"></div>
  <h3 class="section-title" style="left:28px;top:191px">Medical only VS Medical/Indemnity Claims</h3>
  <svg class="abs" style="left:0;top:183px" width="467" height="30"><polyline points="28,30 320,30 345,0 467,0" fill="none" stroke="#2f95d0" stroke-width="1.2"/></svg>
  <svg class="abs" style="left:174px;top:236px" width="130" height="130" viewBox="0 0 130 130">
    <g transform="rotate(-90 65 65)">
      <circle cx="65" cy="65" r="50" fill="none" stroke="#2f95d0" stroke-width="30"/>
      <circle cx="65" cy="65" r="50" fill="none" stroke="#0f1f4b" stroke-width="30" stroke-dasharray="94.2 314.2"/>
    </g>
    <circle cx="65" cy="65" r="35" fill="#fff" stroke="#0f1f4b" stroke-width="1.5"/>
    <text x="65" y="70" text-anchor="middle" font-family="Bebas Neue, sans-serif" font-size="30" fill="#0f1f4b">22</text>
    <text x="65" y="84" text-anchor="middle" font-family="Poppins, sans-serif" font-weight="600" font-size="11" fill="#0f1f4b">CLAIMS</text>
  </svg>
  <svg class="abs" style="left:142px;top:220px" width="185" height="100"><polyline points="0,80 12,80 18,59 40,59" fill="none" stroke="#2f95d0" stroke-width="1"/><polyline points="125,34 150,34 165,4 180,4" fill="none" stroke="#2f95d0" stroke-width="1"/></svg>
  <div class="callout" style="left:49px;top:248px;width:93px;height:104px;background:var(--blue)">
    <div class="hd" style="background:var(--navy)">MEDICAL/INDEMNITY<br>CLAIMS</div>
    <ul><li>$198,904 incurred losses</li><li>0.446 mod impact.</li><li>$267,600 3 year premium impact</li></ul>
  </div>
  <div class="callout" style="left:322px;top:208px;width:94px;height:99px;background:var(--navy)">
    <div class="hd" style="background:var(--blue)">MEDICAL ONLY CLAIMS</div>
    <ul><li>$85,719 incurred losses.</li><li>0.127 mod impact.</li><li>$76,200 3 year premium impact.</li></ul>
  </div>
  <table class="data-table" style="left:47px;top:403px">
    <tr><th style="width:62px">Loss Type</th><th style="width:55px">Loss Amount</th><th style="width:53px">Mod Impact</th><th style="width:68px">3 year premium Impact</th><th style="width:59px">Number Of Claims</th></tr>
    <tr><td>Medical Only</td><td>$85,719</td><td>0.127</td><td>$76,200</td><td>15</td></tr>
    <tr><td>Medical Indemnity</td><td>$198,904</td><td>0.446</td><td>$267,600</td><td>7</td></tr>
  </table>
  <div class="abs" style="left:145px;top:476px;font-size:6.5px;font-weight:600;color:#222">$284,623</div>
  <div class="disclaimer" style="top:522px">DISCLAIMER</div>
  <div class="brand"><i></i>LEDGERWAY</div>
</section>

<section class="page" style="left:80px;top:1532px">
  <div class="page-head"><span class="tab" style="width:246px">CLAIMS BY CAUSE OF INJURY</span></div>
  <p class="abs small" style="left:27px;top:63px;width:400px">Visually grouping the claims together can help with identifying trends and areas to focus on for improvement and future risk management. The following groupings identify the top losses incurred by your company.</p>
  <div class="abs" style="left:0;top:100px;width:467px;height:200px;background:linear-gradient(90deg,#fff 0%,#f0f0f0 60%,#fff 100%)"></div>
  <h3 class="section-title" style="left:27px;top:108px">Claims Grouped By Cause Of Injury</h3>
  <svg class="abs" style="left:0;top:98px" width="467" height="30"><polyline points="27,29 242,29 270,1 467,1" fill="none" stroke="#2f95d0" stroke-width="1.2"/></svg>
  <ul class="legend abs" style="left:27px;top:151px">
    <li><i style="background:var(--blue)"></i>Fall, Slip or Trip Injury</li>
    <li><i style="background:var(--navy)"></i>Cut, Puncture, Scrape</li>
    <li><i style="background:var(--yellow)"></i>Struck or Injured By</li>
    <li><i style="background:var(--mint)"></i>Strain or Injury By</li>
  </ul>
  <ul class="legend abs" style="left:338px;top:151px">
    <li><i style="background:#16294d"></i>Miscellaneous Causes</li>
    <li><i style="background:#2b3fd8"></i>Burn or Scald</li>
    <li><i style="background:var(--red)"></i>Motor Vehicle</li>
  </ul>
  <svg class="abs" style="left:164px;top:149px" width="130" height="130" viewBox="0 0 130 130">
    <g transform="rotate(-90 65 65)" fill="none" stroke-width="30">
      <circle cx="65" cy="65" r="50" stroke="#2f95d0" stroke-dasharray="84.8 314.2"/>
      <circle cx="65" cy="65" r="50" stroke="#0f1f4b" stroke-dasharray="78.5 314.2" stroke-dashoffset="-84.8"/>
      <circle cx="65" cy="65" r="50" stroke="#f8c21a" stroke-dasharray="66 314.2" stroke-dashoffset="-163.3"/>
      <circle cx="65" cy="65" r="50" stroke="#35d07a" stroke-dasharray="31.4 314.2" stroke-dashoffset="-229.3"/>
      <circle cx="65" cy="65" r="50" stroke="#e3221c" stroke-dasharray="37.7 314.2" stroke-dashoffset="-260.7"/>
      <circle cx="65" cy="65" r="50" stroke="#2b3fd8" stroke-dasharray="7.9 314.2" stroke-dashoffset="-298.4"/>
      <circle cx="65" cy="65" r="50" stroke="#16294d" stroke-dasharray="7.9 314.2" stroke-dashoffset="-306.3"/>
    </g>
    <circle cx="65" cy="65" r="35" fill="#fff"/>
    <text text-anchor="middle" font-family="Poppins, sans-serif" font-weight="700" font-size="9" fill="#0f1f4b"><tspan x="65" y="57">CLAIMS BY</tspan><tspan x="65" y="67">CAUSE OF</tspan><tspan x="65" y="77">INJURY</tspan></text>
  </svg>
  <table class="data-table" style="left:27px;top:319px">
    <tr><th style="width:97px">Claim Type</th><th style="width:57px">Number Of Claims</th><th style="width:65px">Claim Amount</th><th style="width:54px">Mod Impact</th><th style="width:70px">3 year premium cost</th></tr>
    <tr><td>Fall, Slip or Trip Injury</td><td>4</td><td>$81,879</td><td>0.137</td><td>$82,200</td></tr>
    <tr><td>Cut, Puncture, Scrape</td><td></td><td></td><td></td><td></td></tr>
    <tr><td>Injured By</td><td>3</td><td>$73,917</td><td>0.130</td><td>$11,400</td></tr>
    <tr><td>Struck or Injured By</td><td>4</td><td>$58,108</td><td>0.087</td><td>$87,600</td></tr>
    <tr><td>Strain or Injury By</td><td>4</td><td>$35,669</td><td>0.146</td><td>$52,200</td></tr>
    <tr><td>Motor Vehicle</td><td>2</td><td>$23,674</td><td>0.032</td><td>$19,200</td></tr>
    <tr><td>Burn or Scald</td><td>4</td><td>$10,426</td><td>0.039</td><td>$23,400</td></tr>
    <tr><td>Miscellaneous Causes</td><td>1</td><td>$950</td><td>0.002</td><td>$1,200</td></tr>
  </table>
  <div class="disclaimer" style="top:522px">DISCLAIMER</div>
  <div class="brand"><i></i>LEDGERWAY</div>
</section>

<section class="page" style="left:660px;top:1532px">
  <div class="page-head"><span class="tab" style="width:246px">CLAIMS BY NATURE OF INJURY</span></div>
  <table class="data-table" style="left:30px;top:61px">
    <tr><th style="width:98px;height:22px">Claim Type</th><th style="width:57px">Number Of Claims</th><th style="width:63px">Claim Amount</th><th style="width:53px">Mod Impact</th><th style="width:70px">3 year premium cost</th></tr>
    <tr><td>All Other Specific Injuries, NOC</td><td>1</td><td>$18,500</td><td>0.025</td><td>$15,000</td></tr>
    <tr><td>Bruising</td><td>2</td><td>$7,759</td><td>0.011</td><td>$6,600</td></tr>
    <tr><td>Burn or Scald</td><td>2</td><td>$2,990</td><td>0.005</td><td>$3,000</td></tr>
    <tr><td>Concussion</td><td>2</td><td>$22,991</td><td>0.031</td><td>$18,600</td></tr>
    <tr><td>Crushing</td><td>2</td><td>$34,115</td><td>0.113</td><td>$67,800</td></tr>
    <tr><td>Heat Prostration</td><td>1</td><td>$950</td><td>0.002</td><td>$1,200</td></tr>
    <tr><td>Laceration</td><td>3</td><td>$73,917</td><td>0.13</td><td>$78,000</td></tr>
    <tr><td>Poisoning</td><td>1</td><td>$7,436</td><td>0.034</td><td>$20,400</td></tr>
    <tr><td>Sprain or Tear</td><td>2</td><td>$5,296</td><td>0.015</td><td>$9,000</td></tr>
    <tr><td>Strain or Tear</td><td>5</td><td>$110,669</td><td>0.087</td><td>$52,200</td></tr>
  </table>
  <div class="band" style="top:287px;height:193px"></div>
  <div class="photo" role="img" aria-label="Photo of business people shaking hands over a signed contract" style="left:38px;top:272px;width:388px;height:193px;background:linear-gradient(120deg,#eef0f3 0%,#c9ced6 35%,#f4f5f7 55%,#2a3347 80%,#d8dce2 100%)"></div>
  <div class="disclaimer" style="top:522px">DISCLAIMER</div>
  <div class="brand"><i></i>LEDGERWAY</div>
</section>

</body>
</html>
```